Tunevia artwork for new single release

I need Tunevia artwork creating to release a new single on there.

The specs are:

Ideal size: 3000 x 3000 pixels
Minimum size: 1400 x 1400 pixels
Aspect ratio: 1:1 (must be a perfect square)
File format: JPG or PNG
Color space: sRGB
File size: Max 4MB

The song is called "Still, Can We Dance?"
The artist is "Milo Brannick"

We have no images of Milo, so it really is open to imagination.

Target Market(s)

Tunevia listeners

Industry/Entity Type

Music

```html
<!DOCTYPE html>
<html lang="en">
<head>
<meta charset="utf-8">
<title>Still, Can We Dance? — Milo Brannick — Single Cover</title>
<link href="https://fonts.googleapis.com/css2?family=Oswald:wght@500&family=Kaushan+Script&family=Cinzel+Decorative:wght@400&display=swap" rel="stylesheet">
<style>
  :root {
    --stage: #414046;
    --board-light: #2e2e30;
    --board-dark: #1c1c1e;
    --title-red: #e04543;
    --chalk-white: #ffffff;
  }
  * { margin: 0; padding: 0; box-sizing: border-box; }
  html, body {
    width: 749px;
    height: 1200px;
    overflow: hidden;
    background: var(--stage);
  }
  .cover {
    position: absolute;
    left: 55px;
    top: 280px;
    width: 640px;
    height: 640px;
    overflow: hidden;
    background: radial-gradient(ellipse at 45% 40%, var(--board-light) 0%, var(--board-dark) 100%);
  }
  .cover__texture {
    position: absolute;
    inset: 0;
  }
  .title {
    position: absolute;
    inset: 0;
  }
  .title__lead {
    position: absolute;
    left: 112px;
    top: 88px;
    font-family: "Kaushan Script", cursive;
    font-size: 64px;
    color: var(--chalk-white);
    transform: rotate(-6deg);
    line-height: 1;
  }
  .title__upper {
    position: absolute;
    left: 228px;
    top: 44px;
    font-family: "Oswald", sans-serif;
    font-weight: 500;
    font-size: 128px;
    line-height: 1;
    color: var(--title-red);
    letter-spacing: -2px;
  }
  .title__main {
    position: absolute;
    left: 0;
    width: 640px;
    top: 178px;
    text-align: center;
    font-family: "Oswald", sans-serif;
    font-weight: 500;
    font-size: 184px;
    line-height: 1;
    color: var(--title-red);
    letter-spacing: -4px;
  }
  .title__tail {
    position: absolute;
    left: 300px;
    top: 368px;
    font-family: "Kaushan Script", cursive;
    font-size: 124px;
    line-height: 1;
    color: var(--chalk-white);
    transform: rotate(-4deg);
  }
  .artist {
    position: absolute;
    left: 0;
    width: 640px;
    top: 568px;
    text-align: center;
    font-family: "Cinzel Decorative", serif;
    font-size: 28px;
    letter-spacing: 10px;
    color: var(--title-red);
    line-height: 1;
  }
</style>
</head>
<body>
  <main class="cover">
    <svg class="cover__texture" role="img" aria-label="Dark chalkboard texture background" width="640" height="640">
      <rect width="640" height="640" fill="transparent"/>
    </svg>
    <h1 class="title">
      <span class="title__lead">Still,</span>
      <span class="title__upper">CAN WE</span>
      <span class="title__main">DANCE</span>
      <span class="title__tail">?</span>
    </h1>
    <p class="artist">MILO BRANNICK</p>
  </main>
</body>
</html>
```